my personal cards just intrducing my self

Massage Therapy to get my name out their

Target Market(s)

40 year olds who enjoy massage

Industry/Entity Type

Massage

Contact Information for Business Card

Leonard T Vasquelle
LMT-Licensed Massage Therapist
*Swedish *Deep Tissue *Prenatal
*Reflexology *Chair and more

(602)-347-2916
leonardvasquelle@mailorbit.net

Font styles to use
Serif

Colors
0456a4
6b449b

```html
<!DOCTYPE html>
<html lang="en">
<head>
<meta charset="utf-8">
<title>Leonard T Vasquelle – Business Card</title>
<link rel="stylesheet" href="https://fonts.googleapis.com/css2?family=Pinyon+Script&family=Raleway:wght@400;500&display=swap">
<style>
  :root {
    --blue: #0456a4;
    --purple: #6b449b;
    --white: #ffffff;
    --backdrop: #e6e6e6;
    --card-w: 560px;
    --card-h: 320px;
  }
  * { box-sizing: border-box; margin: 0; padding: 0; }
  html, body {
    width: 1200px; height: 1000px; overflow: hidden;
    background: var(--backdrop);
  }
  .sheet {
    width: 1200px; height: 1000px;
    display: flex; flex-direction: column; align-items: center; justify-content: center;
    gap: 60px;
  }
  .card {
    position: relative;
    width: var(--card-w); height: var(--card-h);
    border-radius: 22px;
    overflow: hidden;
    box-shadow: 0 6px 18px rgba(0,0,0,0.18);
    font-family: "Raleway", sans-serif;
  }
  .script-name {
    font-family: "Pinyon Script", cursive;
    font-weight: 400;
    white-space: nowrap;
  }

  /* Front */
  .card--front { background: var(--blue); }
  .card--front .script-name {
    position: absolute; left: 0; right: 0; top: 86px;
    text-align: center; padding-left: 40px;
    font-size: 40px; color: var(--white);
  }
  .title-band {
    position: absolute; left: 0; right: 0; top: 148px;
    height: 44px;
    background: var(--purple);
    box-shadow: 0 -5px 0 -1px var(--blue), 0 -7px 0 -1px var(--white),
                0 5px 0 -1px var(--blue), 0 7px 0 -1px var(--white);
    display: flex; align-items: center; justify-content: flex-end;
    padding-right: 42px;
    color: var(--white); font-size: 21px; letter-spacing: 0.5px;
    text-transform: uppercase;
  }
  .title-band::before, .title-band::after {
    content: ""; position: absolute; left: 0; right: 0; height: 2px; background: var(--white);
  }
  .title-band::before { top: -6px; }
  .title-band::after { bottom: -6px; }

  /* Back */
  .card--back { background: var(--white); }
  .services {
    position: absolute; left: 0; right: 0; top: 0; height: 150px;
    background: var(--blue);
    color: var(--white);
    font-size: 27px; letter-spacing: 0.5px; line-height: 32px;
    padding-top: 34px;
  }
  .services__grid {
    display: grid; grid-template-columns: 1fr 1fr; column-gap: 46px;
    width: 430px; margin: 0 auto;
  }
  .services__grid span:nth-child(odd) { text-align: right; }
  .services__more { text-align: center; }
  .contact-band {
    position: absolute; left: 0; right: 0; top: 150px; height: 34px;
    background: var(--purple);
    border-bottom: 2px solid var(--white);
    box-shadow: 0 2px 0 0 var(--purple);
    display: flex; align-items: center; justify-content: space-between;
    padding: 0 22px;
    color: var(--white); font-size: 17px; letter-spacing: 0.3px;
  }
  .contact-band__item { display: flex; align-items: center; gap: 7px; }
  .contact-band__icon { width: 16px; height: 16px; fill: var(--white); }
  .card--back .script-name {
    position: absolute; left: 0; right: 0; top: 212px;
    text-align: center;
    font-size: 44px; color: var(--purple);
  }
</style>
</head>
<body>
<main class="sheet">
  <section class="card card--front" aria-label="Card front">
    <h1 class="script-name">Leonard T Vasquelle</h1>
    <div class="title-band">LMT-Licensed Massage Therapist</div>
  </section>

  <section class="card card--back" aria-label="Card back">
    <div class="services">
      <div class="services__grid">
        <span>SWEDISH</span><span>DEEP TISSUE</span>
        <span>PRENATAL</span><span>REFLEXOLOGY</span>
      </div>
      <div class="services__more">CHAIR AND MORE</div>
    </div>
    <div class="contact-band">
      <span class="contact-band__item">
        <svg class="contact-band__icon" viewBox="0 0 24 24" aria-hidden="true"><path d="M6.6 10.8a15.1 15.1 0 0 0 6.6 6.6l2.2-2.2a1 1 0 0 1 1-.25 11.4 11.4 0 0 0 3.6.57 1 1 0 0 1 1 1V20a1 1 0 0 1-1 1A17 17 0 0 1 3 4a1 1 0 0 1 1-1h3.5a1 1 0 0 1 1 1c0 1.25.2 2.45.57 3.57a1 1 0 0 1-.25 1z"/></svg>
        (602)-347-2916
      </span>
      <span class="contact-band__item">
        <svg class="contact-band__icon" viewBox="0 0 24 24" aria-hidden="true"><path d="M2 5h20v14H2z M2 5l10 8 10-8" fill="none" stroke="#fff" stroke-width="2"/></svg>
        leonardvasquelle@mailorbit.net
      </span>
    </div>
    <p class="script-name">Leonard T Vasquelle</p>
  </section>
</main>
</body>
</html>
```